We need a Glass-Shattering Brochure

We area start up renewable company based in the UK but operate in West Africa. We have a unique blend of local know-how and international exposure to latest solar technology. We pride ourselves in bringing next generation, ground breaking, value for money solar products to Africa.

We are launching a massive campaign to introduce some of the world's best solar product to our high net-worth clients and decision makers. This will be a single brochure of A4 size on 8 pages. Details of the page content is attached.

Also a sample of what we like is attached. The brochure must be clean , fresh, very contemporary and straight to the point - Clear

I have attached a link to some of our installation pictures and some pictures that I think you might need. But feel free to source pictures you think will be appropriate for the intended audience.

You can access some of our paid pictures and installation pictures here https://filedrop-example.net/f/x7KpQm2RtLw9ZvNc4HdYs8BjE

Apologies to everyone. We have just uploaded the brochure content

Target Market(s)

Top company executives

Industry/Entity Type

It Company

Requirements
Must have
• Similar font used in the sample brochure attached. White background. Hint of the green. Please check out our website at www.tolvarpower.co.uk
Nice to have
• Other pictures other than the ones provided

```html
<!DOCTYPE html>
<html lang="en">
<head>
<meta charset="utf-8">
<title>Tolvar Power Brochure Spread</title>
<link href="https://fonts.googleapis.com/css2?family=Jost:wght@400;500&display=swap" rel="stylesheet">
<style>
  :root {
    --backdrop: #efebe4;
    --paper: #ffffff;
    --ink: #2b2b2b;
    --heading-grey: #4a4a4a;
    --brand-green: #0b6b2e;
    --label-black: #262626;
    --gutter-shade: rgba(0,0,0,0.16);
  }
  * { box-sizing: border-box; margin: 0; padding: 0; }
  html, body { width: 1200px; height: 1200px; overflow: hidden; }
  body {
    background: var(--backdrop);
    font-family: "Jost", sans-serif;
    color: var(--ink);
    position: relative;
  }
  .spread {
    position: absolute;
    left: 25px; top: 193px;
    width: 1150px; height: 814px;
    background: var(--paper);
    box-shadow: 0 4px 14px rgba(0,0,0,0.18);
  }
  .page { position: absolute; top: 0; width: 575px; height: 814px; }
  .page--left { left: 0; }
  .page--right { left: 575px; }
  .page--left::after {
    content: "";
    position: absolute; top: 0; right: 0;
    width: 150px; height: 100%;
    background: linear-gradient(to right, rgba(0,0,0,0), var(--gutter-shade));
    pointer-events: none;
  }
  .photo { position: absolute; }
  .photo--rooftop {
    left: 0; top: 41px; width: 575px; height: 358px;
    background: linear-gradient(160deg, #6f8fb8 0%, #3d5a8c 35%, #223a75 60%, #6b6253 100%);
  }
  .photo--sawmill {
    left: 0; top: 41px; width: 575px; height: 358px;
    background: linear-gradient(180deg, #3f5a2c 0%, #587238 35%, #8a6f55 60%, #9b8c78 100%);
  }
  .photo--solar-farm {
    left: 41px; top: 647px; width: 493px; height: 126px;
    background: linear-gradient(180deg, #c9d6df 0%, #8a9e6a 35%, #5b6a86 65%, #a8643c 100%);
  }
  .feature-box { position: absolute; left: 41px; top: 440px; width: 154px; }
  .feature-box__title {
    background: var(--label-black);
    color: #fff;
    font-size: 19.5px;
    font-weight: 400;
    letter-spacing: 0.6px;
    height: 39px;
    line-height: 39px;
    padding-left: 13px;
  }
  .feature-box__body {
    background: var(--brand-green);
    color: #fff;
    height: 156px;
    padding: 13px 12px 13px 13px;
    font-size: 11px;
    line-height: 14px;
    letter-spacing: 0.4px;
  }
  .feature-box__body strong { font-weight: 500; }
  .text-col {
    position: absolute;
    width: 154px;
    font-size: 11px;
    line-height: 14px;
    letter-spacing: 0.4px;
  }
  .text-col p { margin-bottom: 14px; }
  .text-col h3 { font-size: 11px; font-weight: 500; line-height: 14px; }
  .col-l2 { left: 210px; top: 442px; }
  .col-l3 { left: 379px; top: 442px; }
  .section-title {
    position: absolute;
    left: 40px; top: 441px;
    font-size: 23px;
    font-weight: 400;
    color: var(--heading-grey);
    letter-spacing: 0.8px;
  }
  .col-r1 { left: 40px; top: 481px; }
  .col-r2 { left: 210px; top: 481px; }
  .col-r3 { left: 379px; top: 481px; }
</style>
</head>
<body>
  <main class="spread">
    <section class="page page--left">
      <div class="photo photo--rooftop" role="img" aria-label="Installers in hard hats fitting blue solar panels on a pitched roof"></div>

      <div class="feature-box">
        <h2 class="feature-box__title">Talk is Cheap!</h2>
        <div class="feature-box__body">
          <strong>Why Tolvar Power ?</strong> We only do one thing and we make sure we get it 110% right, all the time. We specialise on using next generation, value for money components on all our designs.
        </div>
      </div>

      <div class="text-col col-l2">
        <h3>In Return</h3>
        <p>We will give you 8 year replacement service agreement on all components.</p>
        <p>We will provide near real time online monitoring performance dashboard to let you know how you system is performing. From Battery State of Charge to Power Generated displayed on your tablet or smartphone.</p>
      </div>

      <div class="text-col col-l3">
        <p>We will provide Pay as You Go package to ease the initial cost of setting up</p>
        <h3>Life Span</h3>
        <p>We estimate your product to last 25 years</p>
        <h3>Battery Life Span</h3>
        <p>We will provide a guarantee on our battery supplied to last a minimum 8 years</p>
      </div>

      <div class="photo photo--solar-farm" role="img" aria-label="Wide view of a ground-mounted solar farm on red earth"></div>
    </section>

    <section class="page page--right">
      <div class="photo photo--sawmill" role="img" aria-label="Workers beside a generator-powered sawmill with logs in a forest clearing"></div>

      <h2 class="section-title">Tolvar:SMEs</h2>

      <div class="text-col col-r1">
        <p>Small-Scale Medium Enterprise are the backbone of the African economy providing 80% of its employment workforce. These SME often struggle to provide sustainable business model with the increasing energy crisis.</p>
        <p>Africa's SME are heavily reliant on generators, in other words Africa's economy is totally backed by generators. However current dependency on generators is proving more costly and detrimental to the environment. But with today's advancement in solar technology, we are reversing the conversation from a</p>
      </div>

      <div class="text-col col-r2">
        <p>generator backed economy to solar powered economy</p>
        <p>Tolvar Power has initiated a new product called Power Step Scheme to help SMEs and small businesses get on the ladder of power independence. The product will offer a manageable Pay Us You Go for solar systems from 5kVa to 25kVa. SMEs will have the benefit of having power generation for 24hrs at a cheaper rate than current diesel generators and conventional grid.</p>
        <p>We want to hear from you if you are Small-Scale Medium Enterprise operating any</p>
      </div>

      <div class="text-col col-r3">
        <p>where in Africa. If you are a bakery owner, poultry farmer, cold room store operative. If you consider your business as a small business, and you want to stop using the noisy, erratic generator. If you want to have access to electricity round the clock 365 days at a cheaper rate, we want to support that vision.</p>
      </div>
    </section>
  </main>
</body>
</html>
```